Business Card Design

​Silver Harbor Grooves provides personal, friendly service in a fun and high energy environment. We are based in Vermont.

We would like a card that appeals to a wide range of audiences as we do a wide range of events. Please feel free to check out our website silverharborgrooves.com for inspiration.

Target Market(s)

weddings, corporate, birthday parties, colleges

Industry/Entity Type

Business

Contact Information for Business Card

Silver Harbor Grooves
Providing Entertainment For All Occasions
555 218 6093
silverharborgrooves@mailvane.com
silverharborgrooves.com

```html
<!DOCTYPE html>
<html lang="en">
<head>
<meta charset="utf-8">
<title>Silver Harbor Grooves – Business Card</title>
<link href="https://fonts.googleapis.com/css2?family=Roboto+Condensed:wght@400;700&display=swap" rel="stylesheet">
<style>
  :root {
    --bg: #e9e6e2;
    --paper: #ffffff;
    --green: #17724a;
    --green-dark: #0f5a39;
    --maroon: #8e1f24;
    --red: #c0393c;
    --ink: #1d1d1d;
  }
  * { margin: 0; padding: 0; box-sizing: border-box; }
  html, body {
    width: 1200px; height: 913px; overflow: hidden;
    background: var(--bg);
    font-family: "Roboto Condensed", "Arial Narrow", sans-serif;
  }
  .canvas { position: relative; width: 1200px; height: 913px; }
  .card {
    position: absolute;
    width: 520px; height: 297px;
    background: var(--paper);
    box-shadow: 0 6px 18px rgba(0,0,0,.18);
    overflow: hidden;
  }
  .card--front { left: 60px; top: 150px; }
  .card--back  { left: 620px; top: 466px; }

  .brand {
    display: flex; align-items: center; gap: 12px;
    color: var(--green); font-weight: 700; text-transform: uppercase;
    letter-spacing: 1px; white-space: nowrap;
  }
  .brand__mark { width: 14px; height: 14px; background: var(--green); flex: none; }
  .card--front .brand {
    position: absolute; left: 0; right: 0; top: 128px;
    justify-content: center; font-size: 34px;
  }
  .card--front .brand__mark { width: 22px; height: 22px; }

  .card--back .brand {
    position: absolute; left: 150px; top: 26px; font-size: 18px; gap: 10px;
  }
  .swoosh { position: absolute; inset: 0; width: 520px; height: 297px; }

  .tagline {
    position: absolute; right: 16px; top: 104px;
    color: #fff; font-weight: 700; font-size: 13px; line-height: 1.45;
    text-align: right; white-space: nowrap;
  }
  .contacts {
    position: absolute; left: 22px; bottom: 44px;
    list-style: none; color: var(--ink); font-weight: 700; font-size: 14px;
  }
  .contacts li { display: flex; align-items: center; gap: 8px; margin-top: 6px; white-space: nowrap; }
  .contacts svg { width: 14px; height: 14px; fill: var(--green-dark); flex: none; }
</style>
</head>
<body>
<main class="canvas">

  <section class="card card--front" aria-label="Card front">
    <div class="brand"><span class="brand__mark"></span>Silver Harbor Grooves</div>
  </section>

  <section class="card card--back" aria-label="Card back">
    <svg class="swoosh" viewBox="0 0 520 297" aria-hidden="true">
      <path d="M520 40 C400 45 345 100 330 170 C318 235 290 275 240 297 L520 297 Z" fill="var(--green)"/>
      <path d="M520 28 C395 33 333 90 318 165 C306 232 275 275 215 297" fill="none" stroke="var(--maroon)" stroke-width="7"/>
      <path d="M520 18 C388 22 321 82 306 160 C294 228 262 272 195 297" fill="none" stroke="var(--red)" stroke-width="2"/>
    </svg>

    <div class="brand"><span class="brand__mark"></span>Silver Harbor Grooves</div>

    <p class="tagline">Silver Harbor Grooves<br>Providing Entertainment<br>For All Occasions</p>

    <ul class="contacts">
      <li>
        <svg viewBox="0 0 16 16"><path d="M2 5c0-2 2-3 6-3s6 1 6 3v1h-3V5H5v1H2z M4 7h8l2 7H2z"/></svg>
        555 218 6093
      </li>
      <li>
        <svg viewBox="0 0 16 16"><path d="M1 3h14v10H1z M1 3l7 6 7-6" stroke="#fff" stroke-width="1"/></svg>
        silverharborgrooves@mailvane.com
      </li>
      <li>
        <svg viewBox="0 0 16 16"><circle cx="8" cy="8" r="7"/><path d="M1 8h14 M8 1c-3 4-3 10 0 14 M8 1c3 4 3 10 0 14" stroke="#fff" stroke-width="1" fill="none"/></svg>
        www.silverharborgrooves.com
      </li>
    </ul>
  </section>

</main>
</body>
</html>
```